Hello,
We’re looking for a new WordPress website for Gather Your Light, our company offering unique well-being retreats and workshops.
We currently have a website online (you can consult it : www.gatheryourlight.ch), but we now need to build a new site on WordPress — more flexible, more intuitive to manage, and better aligned with our evolving needs.

What we’re looking for:
A new userfriendly WordPress site, with:
Inspiring, elegant, and modern design
Smooth user experience on desktop and mobile
Innovative design proposals – we want to be inspired !
SEO best practices
Respect of our existing color palette
The final website will need to be set up on our existing hosting provider (details can be shared later)

Pages to Include:
- Home
- Our Story
- Our Stays - with links to 5 individual pages, each describing one of our stays in detail.
- Activities – with potential links to individual descriptive pages
- Agenda
- Our Charter
- The Team
- Contact
- Blog

Required Features:
- Space for photos and videos
- Sections for testimonials and press articles
- Blog/article layout with strong readability
- Easy-to-update backend for future content
- Newsletter sign-up (pop-up and in footer)
- Additional pop-up on/off
- “Request info” buttons
- “Booking request” buttons
- Integration of our 4 pillars - Breathe · Feel · Connect · Experience - in the design (They’re currently in the footer, but we’re open to creative suggestions)

Who we are :
Gather Your Light offers well-being and personal growth stays but with a very different spirit.
We’re not a classic wellness brand. Our approach is professional, joyful, and grounded.
We create spaces where people can take a real break — breathe, slow down, and reconnect with themselves.
During our stays, people are welcomed like friends:
with warmth, respect, and no pressure.
Each program combines practices like breathwork, movement, creativity, coaching, and massages in a relaxed, beautiful setting of the French Alps.
What makes us different:
A friendly and down-to-earth atmosphere
A wide mix of activities.
A mix of inner work and simple pleasures
Private rooms, nourishing food, and shared moments
Time to talk, to laugh, to walk, or just be silent together - and feel free to be yourself
Our guests come to pause.
They leave feeling lighter, aligned, and full of life

```html
<!DOCTYPE html>
<html lang="fr">
<head>
<meta charset="utf-8">
<title>Gather Your Light – Reprendre son souffle</title>
<link href="https://fonts.googleapis.com/css2?family=Libre+Caslon+Text:wght@400;700&family=Poppins:wght@400;500;600&display=swap" rel="stylesheet">
<style>
:root{
  --teal:#6cc5c0;
  --teal-soft:#eef7f8;
  --navy:#1c3f94;
  --ink:#1f2430;
  --text:#5b6170;
  --muted:#8a909c;
  --dark:#2f3033;
  --white:#ffffff;
  --serif:"Libre Caslon Text", Georgia, serif;
  --sans:"Poppins", Arial, sans-serif;
}
*{box-sizing:border-box;margin:0;padding:0}
html,body{width:1200px;height:4898px;overflow:hidden}
body{font-family:var(--sans);color:var(--text);background:var(--white);position:relative}
section,header,footer,.topbar{position:absolute;left:0;width:1200px}
.abs{position:absolute}
.label{position:absolute;font-size:12px;letter-spacing:1.5px;text-transform:uppercase;color:var(--teal);font-weight:500}
.title{position:absolute;font-family:var(--serif);font-size:38px;color:var(--ink);font-weight:400;line-height:1.25}
.center{left:0;width:1200px;text-align:center}
.btn{position:absolute;display:flex;align-items:center;justify-content:center;background:var(--navy);color:var(--white);font-size:12px;font-weight:600;letter-spacing:.5px;text-transform:uppercase}
.photo{position:absolute}

/* top bar */
.topbar{top:0;height:42px;background:var(--teal);color:var(--white);font-size:11px}
.topbar .contact{position:absolute;top:0;height:42px;display:flex;align-items:center;gap:6px}
.topbar .tb-btn{position:absolute;top:0;height:38px;display:flex;align-items:center;justify-content:center;font-size:11px;color:var(--white)}
/* nav */
.nav{top:42px;height:70px;background:var(--white)}
.brand{position:absolute;left:141px;top:10px;text-align:center;color:var(--navy)}
.brand .name{font-size:33px;font-weight:600;letter-spacing:1px;line-height:36px}
.brand .tag{font-size:7px;letter-spacing:6px;text-transform:uppercase;line-height:10px}
.menu{position:absolute;left:411px;top:0;height:70px;display:flex;align-items:center;gap:28px;font-size:12px;color:var(--dark)}
.menu .active{color:var(--navy);font-weight:600}

/* hero */
.hero{top:112px;height:550px;background:radial-gradient(ellipse at 62% 40%,#a08a78 0%,#4a3426 35%,#24170f 70%),#2b1b12}
.hero .shade{position:absolute;inset:0;background:linear-gradient(90deg,rgba(20,12,8,.55),rgba(20,12,8,0) 55%),linear-gradient(0deg,#8a3f12 0%,rgba(138,63,18,0) 30%)}
.hero h1{position:absolute;left:143px;top:250px;font-family:var(--serif);font-weight:700;font-size:62px;line-height:66px;color:var(--white);text-transform:uppercase}
.hero p{position:absolute;left:141px;top:394px;width:430px;font-size:16px;line-height:27px;color:var(--white)}
.hero .cta{position:absolute;left:141px;top:468px;width:182px;height:38px;border-radius:19px;background:var(--teal);color:var(--white);font-size:11px;display:flex;align-items:center;justify-content:center}
.hero .play{position:absolute;left:332px;top:468px;display:flex;align-items:center;gap:10px;color:var(--white);font-size:11px}
.hero .play span.c{width:38px;height:38px;border-radius:50%;border:3px solid var(--teal);background:var(--white);display:flex;align-items:center;justify-content:center}

/* about */
.about{top:662px;height:738px}
.frame-tl{position:absolute;background:var(--teal)}
.about p{position:absolute;left:639px;top:369px;width:445px;font-size:12.5px;line-height:22.5px}
.deco{position:absolute;border-radius:50%;background:radial-gradient(circle,rgba(108,197,192,.35),rgba(108,197,192,0) 70%)}

/* pillars */
.pillars{top:1400px;height:472px;background:var(--teal-soft)}
.pillar{position:absolute;top:203px;width:160px;text-align:center}
.pillar .blob{width:160px;height:140px;background:var(--white);border-radius:50% 50% 46% 54% / 55% 55% 45% 45%;box-shadow:0 6px 0 -2px rgba(108,197,192,.35);display:flex;align-items:center;justify-content:center}
.pillar .name{margin-top:30px;font-family:var(--serif);font-size:20px;color:var(--ink)}

/* stays */
.stays{top:1872px;height:658px}
.stay{position:absolute;top:213px;width:311px}
.stay .ph{height:239px}
.stay h3{margin-top:22px;font-family:var(--serif);font-size:15px;font-weight:700;letter-spacing:.5px;color:var(--ink)}
.stay span{display:block;margin-top:4px;font-size:12px;color:var(--muted)}
.dots{position:absolute;display:flex;align-items:center;gap:16px}
.dots i{width:5px;height:5px;border-radius:50%;background:#c3c8d0;display:block}
.dots i.on{width:26px;height:26px;border:1.5px solid var(--navy);background:transparent;position:relative}
.dots i.on:after{content:"";position:absolute;left:9px;top:9px;width:5px;height:5px;border-radius:50%;background:var(--navy)}

/* distinct */
.distinct{top:2530px;height:637px}
.checks{position:absolute;left:112px;top:172px;width:440px;list-style:none;font-size:12.5px;line-height:23px}
.checks li{display:flex;gap:12px;margin-bottom:12px}
.checks li svg{flex:none;margin-top:3px}

/* testimonials */
.testimonials{top:3167px;height:551px;background:var(--teal-soft)}
.card{position:absolute;top:190px;width:445px;height:219px;background:var(--white);border:1px solid #dfe6ea;padding:30px 28px}
.card p{font-size:12px;line-height:25px}
.card .who{position:absolute;left:28px;bottom:28px;display:flex;align-items:center;gap:14px;font-size:14px;font-weight:500;color:var(--ink)}
.avatar{width:40px;height:40px;border-radius:50%;display:block}
.stars{position:absolute;right:62px;bottom:40px;display:flex;gap:4px}
.qbadge{position:absolute;right:-16px;bottom:-22px;width:42px;height:42px;border-radius:50%;background:var(--navy);display:flex;align-items:center;justify-content:center;color:var(--white);font-family:var(--serif);font-size:30px;font-weight:700;line-height:1}

/* blog */
.blog{top:3718px;height:714px}
.meta{display:flex;align-items:center;gap:8px;font-size:11px;color:var(--muted)}
.meta .av{width:22px;height:22px;border-radius:50%;background:#c9b9a8}
.meta .tag{background:#e4f4f3;color:var(--teal);padding:3px 9px;font-size:10px}
.post-main{position:absolute;left:141px;top:213px;width:441px;height:409px;background:var(--white);box-shadow:0 4px 24px rgba(20,40,80,.08)}
.post-main h4{font-size:15px;font-weight:600;line-height:22px;color:var(--ink)}
.post-side{position:absolute;left:620px;width:440px;height:97px}
.post-side .th{position:absolute;left:0;top:0;width:129px;height:97px}
.post-side .body{position:absolute;left:147px;top:12px;width:290px}
.post-side h4{margin-top:10px;font-size:13px;font-weight:600;line-height:20px;color:var(--ink)}

/* footer */
.footer{top:4432px;height:466px;background:var(--teal);color:var(--white)}
.footer h5{position:absolute;font-size:14px;font-weight:500}
.footer ul{position:absolute;list-style:none;font-size:11px;line-height:31px}
.social{position:absolute;left:141px;top:146px;display:flex;gap:14px}
.social i{display:block;width:26px;height:26px;border-radius:50%;border:1.5px solid var(--white)}
.social i.fill{background:var(--navy);border-color:var(--navy)}
.newsletter{position:absolute;left:141px;top:258px;width:260px;height:40px;border-radius:20px;background:var(--white);color:var(--muted);font-size:12px;display:flex;align-items:center;padding-left:22px}
.newsletter .go{position:absolute;right:4px;top:4px;width:32px;height:32px;border-radius:50%;background:var(--navy);display:flex;align-items:center;justify-content:center}
.reach{position:absolute;left:863px;font-size:11px;display:flex;gap:12px;line-height:16px}
.reach .ic{flex:none;width:26px;height:26px;border-radius:50%;border:1.5px solid var(--white);display:flex;align-items:center;justify-content:center}
.footer .rule{position:absolute;left:112px;top:393px;width:976px;height:1px;background:rgba(255,255,255,.45)}
.footer .legal{position:absolute;top:424px;font-size:10px}
</style>
</head>
<body>

<div class="topbar">
  <div class="contact" style="left:140px">
    <svg width="13" height="13" viewBox="0 0 24 24" fill="none" stroke="#fff" stroke-width="2"><path d="M5 3h4l2 5-3 2a12 12 0 0 0 6 6l2-3 5 2v4a2 2 0 0 1-2 2A17 17 0 0 1 3 5a2 2 0 0 1 2-2z"/></svg>
    +41 58 200 47 20
  </div>
  <div class="contact" style="left:272px">
    <svg width="15" height="12" viewBox="0 0 24 18" fill="none" stroke="#fff" stroke-width="2"><rect x="1" y="1" width="22" height="16"/><path d="M1 1l11 9 11-9"/></svg>
    info@gatheryourlight.ch
  </div>
  <div class="tb-btn" style="left:730px;width:162px;background:var(--dark)">Demande d'information</div>
  <div class="tb-btn" style="left:901px;width:158px;background:var(--navy)">Demande de réservation</div>
</div>

<header class="nav">
  <div class="brand"><div class="name">GATHER</div><div class="tag">your light</div></div>
  <nav class="menu">
    <span class="active">Accueil</span><span>Notre histoire</span><span>Nos séjours</span><span>Activités</span><span>Ordre du jour</span><span>Notre charte</span><span>Blog</span><span>Contact</span>
  </nav>
</header>

<section class="hero" role="img" aria-label="Photo : personne méditant en tailleur dans une salle en bois éclairée par une fenêtre au coucher du soleil">
  <div class="shade"></div>
  <h1>Reprendre<br>son souffle</h1>
  <p>Retraites de bien-être et de croissance personnelle dans les Alpes françaises</p>
  <div class="cta">Demande de réservation</div>
  <div class="play"><span class="c"><svg width="12" height="14" viewBox="0 0 12 14"><path d="M1 1l10 6-10 6z" fill="#6cc5c0"/></svg></span>Voir la vidéo</div>
</section>

<section class="about">
  <div class="frame-tl" style="left:112px;top:121px;width:312px;height:10px"></div>
  <div class="frame-tl" style="left:112px;top:121px;width:10px;height:400px"></div>
  <div class="photo" role="img" aria-label="Photo : groupe d'amis assis dans l'herbe en souriant" style="left:122px;top:131px;width:424px;height:514px;background:linear-gradient(180deg,#5d7a33 0%,#8aa54a 30%,#b7b9b8 55%,#6d8e3c 80%,#4f6b25 100%)"></div>
  <div class="deco" role="img" aria-label="Décor : pissenlit stylisé" style="left:1040px;top:80px;width:120px;height:120px"></div>
  <div class="label" style="left:639px;top:230px">Qui nous sommes</div>
  <div class="title" style="left:639px;top:254px;width:460px">Un autre regard sur le bien-être”</div>
  <p>Gather Your Light propose des séjours bien-être et de développement personnel, mais avec un esprit très différent. Nous ne sommes pas une marque de bien-être classique. Notre approche est professionnelle, joyeuse et pragmatique.</p>
  <div class="btn" style="left:639px;top:496px;width:158px;height:44px">En savoir plus</div>
</section>

<section class="pillars">
  <div class="label center" style="top:74px">4 piliers</div>
  <div class="title center" style="top:112px">Un chemin vers plus de présence et de liberté</div>
  <svg class="abs" style="left:0;top:200px" width="1200" height="130" fill="none" stroke="#9aa5b5" stroke-width="1.3" stroke-dasharray="4 4">
    <path d="M255 40 C300 5 360 5 405 30"/>
    <path d="M530 110 C580 135 630 130 680 105"/>
    <path d="M800 40 C850 0 910 5 950 30"/>
  </svg>
  <div class="pillar" style="left:108px"><div class="blob">
    <svg width="60" height="60" viewBox="0 0 60 60" fill="none" stroke="#1c3f94" stroke-width="2"><path d="M22 54V42c-6-3-10-9-10-16a16 16 0 0 1 32 0l4 8h-4v6a4 4 0 0 1-4 4h-4v10"/><path d="M50 14l6-4M51 22h7M50 30l6 4"/></svg>
  </div><div class="name">Respirer</div></div>
  <div class="pillar" style="left:382px"><div class="blob">
    <svg width="60" height="60" viewBox="0 0 60 60" fill="none" stroke="#6cc5c0" stroke-width="2"><circle cx="30" cy="32" r="20"/><path d="M20 36h20M30 6v4M18 10l2 3M42 10l-2 3"/></svg>
  </div><div class="name">Ressentir</div></div>
  <div class="pillar" style="left:656px"><div class="blob">
    <svg width="70" height="60" viewBox="0 0 70 60" fill="none" stroke="#1c3f94" stroke-width="2"><circle cx="18" cy="24" r="6"/><circle cx="35" cy="20" r="7"/><circle cx="52" cy="24" r="6"/><path d="M8 52V38a10 10 0 0 1 20 0v14M25 52V36a10 10 0 0 1 20 0v16M42 52V38a10 10 0 0 1 20 0v14"/><path d="M35 4l3 3-3 3-3-3z"/></svg>
  </div><div class="name">Se Connecter</div></div>
  <div class="pillar" style="left:930px"><div class="blob">
    <svg width="60" height="60" viewBox="0 0 60 60" fill="none" stroke="#6cc5c0" stroke-width="2"><circle cx="30" cy="32" r="22"/><path d="M20 52a10 10 0 0 1 20 0"/><circle cx="30" cy="36" r="6"/><path d="M18 12l2 4 4 .5-3 3 1 4-4-2-4 2 1-4-3-3 4-.5zM42 12l2 4 4 .5-3 3 1 4-4-2-4 2 1-4-3-3 4-.5z"/></svg>
  </div><div class="name">Expérience</div></div>
</section>

<section class="stays">
  <div class="label center" style="top:96px">Séjours</div>
  <div class="title center" style="top:138px">Trouvez votre prochain séjour</div>
  <div class="stay" style="left:112px"><div class="ph" role="img" aria-label="Photo : pavillon en bois au bord d'un lac avec matelas de yoga" style="background:linear-gradient(180deg,#8a5534 0%,#c9c2b8 40%,#6aa0b5 65%,#b44a3c 100%)"></div><h3>ENVOLÉE</h3><span>6 nuits</span></div>
  <div class="stay" style="left:445px"><div class="ph" role="img" aria-label="Photo : tente de glamping illuminée la nuit" style="background:linear-gradient(160deg,#13213d 0%,#2b3a52 35%,#d99a4b 60%,#6b4a2d 100%)"></div><h3>ECHAPPÉE</h3><span>4 nuits</span></div>
  <div class="stay" style="left:778px"><div class="ph" role="img" aria-label="Photo : cabane dans les arbres éclairée au crépuscule" style="background:linear-gradient(180deg,#33506a 0%,#2d4a3a 45%,#6a4a2a 70%,#1d2a1f 100%)"></div><h3>PARENTHÈSE</h3><span>2 nuits</span></div>
  <div class="dots" style="left:543px;top:559px"><i></i><i></i><i class="on"></i><i></i><i></i></div>
</section>

<section class="distinct">
  <div class="label" style="left:112px;top:74px">Une approche à part</div>
  <div class="title" style="left:112px;top:102px">Ce qui nous distingue</div>
  <div class="deco" role="img" aria-label="Décor : pissenlit stylisé" style="left:540px;top:40px;width:90px;height:90px"></div>
  <ul class="checks">
    <li><svg width="18" height="18" viewBox="0 0 18 18" fill="none" stroke="#1c3f94" stroke-width="1.6"><circle cx="9" cy="9" r="8"/><path d="M5 9l3 3 5-6"/></svg>Une ambiance conviviale et authentique.</li>
    <li><svg width="18" height="18" viewBox="0 0 18 18" fill="none" stroke="#1c3f94" stroke-width="1.6"><circle cx="9" cy="9" r="8"/><path d="M5 9l3 3 5-6"/></svg>Une grande variété d'activités.</li>
    <li><svg width="18" height="18" viewBox="0 0 18 18" fill="none" stroke="#1c3f94" stroke-width="1.6"><circle cx="9" cy="9" r="8"/><path d="M5 9l3 3 5-6"/></svg>Un mélange de travail intérieur et de plaisirs simples.</li>
    <li><svg width="18" height="18" viewBox="0 0 18 18" fill="none" stroke="#1c3f94" stroke-width="1.6"><circle cx="9" cy="9" r="8"/><path d="M5 9l3 3 5-6"/></svg>Chambres individuelles, repas copieux et moments partagés.</li>
    <li><svg width="18" height="18" viewBox="0 0 18 18" fill="none" stroke="#1c3f94" stroke-width="1.6"><circle cx="9" cy="9" r="8"/><path d="M5 9l3 3 5-6"/></svg><span>Un moment pour discuter, rire, se promener ou simplement se taire ensemble – et se sentir libre d'être soi-même.<br>Nos hôtes viennent pour faire une pause.</span></li>
    <li><svg width="18" height="18" viewBox="0 0 18 18" fill="none" stroke="#1c3f94" stroke-width="1.6"><circle cx="9" cy="9" r="8"/><path d="M5 9l3 3 5-6"/></svg>Ils repartent plus légers, plus équilibrés et pleins de vie.</li>
  </ul>
  <div class="btn" style="left:112px;top:450px;width:227px;height:44px">Demande de réservation</div>
  <div class="frame-tl" style="left:777px;top:20px;width:310px;height:10px"></div>
  <div class="frame-tl" style="left:1077px;top:20px;width:10px;height:300px"></div>
  <div class="photo" role="img" aria-label="Photo : groupe d'amis riant, assis dans l'herbe au soleil" style="left:654px;top:28px;width:426px;height:516px;background:linear-gradient(180deg,#6a7f35 0%,#93a84c 30%,#b9bcc0 55%,#70903c 80%,#4d6822 100%)"></div>
</section>

<section class="testimonials">
  <div class="label center" style="top:80px">Nos témoignages</div>
  <div class="title center" style="top:118px">Voici ce que disent nos clients</div>
  <svg class="abs" style="left:1072px;top:62px" width="70" height="70" viewBox="0 0 70 70" fill="none" stroke="#6cc5c0" stroke-width="2"><path d="M4 30c0-14 8-24 22-26l2 6c-8 2-12 8-12 14h12v30H4z"/><path d="M40 30c0-14 8-24 22-26l2 6c-8 2-12 8-12 14h12v30H40z"/></svg>
  <div class="card" style="left:141px">
    <p>Lorem Ipsum is simply dummy text of the printintypesetting industry. Lorem Ipsum has been the industry's standdummy text ever since the 1500s, when an unknown printer togalley of type and scrambled it to make a type</p>
    <div class="who"><span class="avatar" role="img" aria-label="Portrait de la cliente" style="background:#e7c9a8"></span>Lina Morel</div>
    <div class="stars"><svg width="88" height="14" viewBox="0 0 88 14" fill="#6cc5c0"><path id="s" d="M7 0l2 4.5 5 .5-3.8 3.3 1.1 4.9L7 10.6 2.7 13.2l1.1-4.9L0 5l5-.5z"/><use href="#s" x="18"/><use href="#s" x="36"/><use href="#s" x="54"/><use href="#s" x="72"/></svg></div>
    <div class="qbadge">”</div>
  </div>
  <div class="card" style="left:614px">
    <p>Lorem Ipsum is simply dummy text of the printintypesetting industry. Lorem Ipsum has been the industry's standdummy text ever since the 1500s, when an unknown printer togalley of type and scrambled it to make a type</p>
    <div class="who"><span class="avatar" role="img" aria-label="Portrait de la cliente" style="background:#5a4636"></span>Claire Dubois</div>
    <div class="stars"><svg width="88" height="14" viewBox="0 0 88 14" fill="#6cc5c0"><path id="s2" d="M7 0l2 4.5 5 .5-3.8 3.3 1.1 4.9L7 10.6 2.7 13.2l1.1-4.9L0 5l5-.5z"/><use href="#s2" x="18"/><use href="#s2" x="36"/><use href="#s2" x="54"/><use href="#s2" x="72"/></svg></div>
    <div class="qbadge">”</div>
  </div>
  <div class="dots" style="left:543px;top:456px"><i></i><i></i><i class="on"></i><i></i><i></i></div>
</section>

<section class="blog">
  <div class="label" style="left:145px;top:94px">Notre blog</div>
  <div class="title" style="left:141px;top:130px">Articles,et actualités</div>
  <div class="btn" style="left:903px;top:109px;width:156px;height:45px">Explorez tout</div>
  <div class="post-main">
    <div role="img" aria-label="Photo : femme respirant les bras ouverts en pleine nature" style="position:absolute;left:11px;top:12px;width:419px;height:224px;background:linear-gradient(135deg,#f2ead8 0%,#c7b78c 40%,#8c7a4f 70%,#c46a3a 100%)"></div>
    <div style="position:absolute;left:20px;top:256px" class="meta"><span class="av"></span>Nora Vallet · ◷ 3 Min To Read · <span class="tag">Breathe</span></div>
    <div style="position:absolute;left:20px;top:296px;width:400px"><h4>Pourquoi Respirer Peut Être Votre Acte Le Plus Productif</h4>
    <p style="margin-top:12px;font-size:10.5px;line-height:20px">Jesus, I pray for my uncle's health and a successful surgery for him. Please protect him and surround him with your saints and</p></div>
  </div>
  <div class="post-side" style="top:213px"><div class="th" role="img" aria-label="Photo : groupe assis sur un banc en bois" style="background:linear-gradient(180deg,#7d9a5e,#b9a987 60%,#7a5a3b)"></div>
    <div class="body"><div class="meta"><span class="av"></span>Marc Fontaine · ◷ 22 Min · <span class="tag">Breathe</span></div><h4>Ce Qui Rend Nos Retraites Différentes des Séjours Bien-Être Classiques</h4></div></div>
  <div class="post-side" style="top:367px"><div class="th" role="img" aria-label="Photo : chalet sous un arc-en-ciel dans la forêt" style="background:linear-gradient(180deg,#8fa7b3,#5e7d4a 55%,#b0503a)"></div>
    <div class="body"><div class="meta"><span class="av"></span>Marc Fontaine · ◷ 12 Min · <span class="tag">Breathe</span></div><h4>7 Signes Que Vous Êtes Peut-être Prêt.e Pour Une Retraite Bien-Être</h4></div></div>
  <div class="post-side" style="top:519px"><div class="th" role="img" aria-label="Photo : randonneur contemplant les montagnes" style="background:linear-gradient(180deg,#a9b4bd,#6f7f86 55%,#3c4a4c)"></div>
    <div class="body"><div class="meta"><span class="av"></span>Nora Vallet · ◷ 8 Min · <span class="tag">Breathe</span></div><h4>Une Journée Type Apaisante et Ressourçante Lors de Nos Retraites</h4></div></div>
</section>

<footer class="footer">
  <div class="brand" style="top:68px;color:var(--white)"><div class="name">GATHER</div><div class="tag">your light</div></div>
  <div class="social"><i></i><i class="fill"></i><i></i></div>
  <h5 style="left:141px;top:224px">S'abonner à la newsletter</h5>
  <div class="newsletter">Entrez votre adresse e-mail
    <span class="go"><svg width="14" height="14" viewBox="0 0 14 14" fill="none" stroke="#fff" stroke-width="2"><path d="M2 7h10M8 3l4 4-4 4"/></svg></span></div>
  <h5 style="left:496px;top:72px">Liens rapides</h5>
  <ul style="left:496px;top:108px"><li>Accueil</li><li>Notre histoire</li><li>Activités</li><li>Agenda</li><li>Notre charte</li><li>L'équipe</li><li>Blog</li><li>Contact</li></ul>
  <h5 style="left:685px;top:72px">Nos Séjours</h5>
  <ul style="left:685px;top:108px"><li>Envolée</li><li>Echappée</li><li>Parenthèse</li><li>Pause</li><li>Instant</li></ul>
  <h5 style="left:863px;top:72px">Restez connectés</h5>
  <div class="reach" style="top:114px"><span class="ic"><svg width="12" height="12" viewBox="0 0 24 24" fill="none" stroke="#fff" stroke-width="2"><path d="M5 3h4l2 5-3 2a12 12 0 0 0 6 6l2-3 5 2v4a2 2 0 0 1-2 2A17 17 0 0 1 3 5a2 2 0 0 1 2-2z"/></svg></span><span style="padding-top:5px">+41 58 200 47 20</span></div>
  <div class="reach" style="top:156px"><span class="ic"><svg width="12" height="10" viewBox="0 0 24 18" fill="none" stroke="#fff" stroke-width="2"><rect x="1" y="1" width="22" height="16"/><path d="M1 1l11 9 11-9"/></svg></span><span style="padding-top:5px">info@gatheryourlight.ch</span></div>
  <div class="reach" style="top:198px"><span class="ic"><svg width="11" height="13" viewBox="0 0 20 24" fill="none" stroke="#fff" stroke-width="2"><path d="M10 23s8-8 8-14a8 8 0 0 0-16 0c0 6 8 14 8 14z"/><circle cx="10" cy="9" r="3"/></svg></span><span>Gather Your Light Sàrl<br>Chemin des Prés 14<br>Bâtiment B2 CH - 1260 Nyon</span></div>
  <div class="rule"></div>
  <div class="legal" style="left:118px">© 2025 Gather Your Light - creation by <u>Studio Lumen</u></div>
  <div class="legal" style="left:817px">Privacy Policy</div>
  <div class="legal" style="left:916px">Cookie Policy</div>
  <div class="legal" style="left:1015px">Terms of Use</div>
</footer>

</body>
</html>
```